Small Ecommerce Styled Site to Sell / Lease Domain Names

We have a small portfolio of 100+ domain names that we would like to offer for sale or lease via a web site. Along the lines of http://www.velmorhosts.example/searchdomain.html?priceChoice=2&sort=leasing_desc

We would like initially a 4 page design, listing page (as site referenced above), domain info page (Corvane Domain Name Landing Page with form) and checkout a page and About Us Page

We do not want a replica of the site listed, please use it as a guide only, we are looking for a fresh design, in similar concept web 2.0

Our Colours are #351a41 (Main) - #ffca27 (Secondary) all other colours must compliment those 2.
Updates

Domain Landing Page:  I am sorry I was not clear about expectations, however we would like a domain landing page that would be the default holding page for a domain name.

For some examples of what I mean please see:
https://www.qarsibex.example.au/guest-articles/7626-domain-for-sale-landing-pages.html
http://dev.plinthwardexchange.example/blog/2013/09/sales-only-landers-and-buy-it-now-2/

Industry/Entity Type

Domain

Font styles to use
Sans Serif

```html
<!DOCTYPE html>
<html lang="en">
<head>
<meta charset="utf-8">
<title>Corvane Domain – Lease Domains</title>
<link rel="stylesheet" href="https://fonts.googleapis.com/css2?family=Arimo:wght@400;700&family=Oswald:wght@500;600&family=Questrial&display=swap">
<style>
:root{
  --plum:#351a41;
  --plum-row:#3f2150;
  --plum-soft:#4a2a5a;
  --gold:#ffca27;
  --gold-deep:#f0a90e;
  --gold-pale:#fff6a8;
  --ink:#333;
  --link:#1d3f7a;
  --red:#cc1111;
  --panel:#eeeeee;
}
*{box-sizing:border-box;margin:0;padding:0}
html,body{width:981px;height:1200px;overflow:hidden;background:#fff;font-family:Arimo,Arial,sans-serif;color:var(--ink)}
.page{position:relative;width:981px;height:1200px}
.abs{position:absolute}

/* top bar */
.topbar{left:0;top:0;width:981px;height:29px;background:linear-gradient(#3a3a3a,#111)}
.topbar a{position:absolute;top:8px;font-size:11px;color:#ddd;text-decoration:none}
.topbar .active{color:var(--gold);font-weight:700}
.social{display:flex;gap:3px;position:absolute;top:5px}
.social span{width:18px;height:18px;border-radius:50%;background:#fff;display:block}

/* header */
.header{left:0;top:29px;width:981px;height:335px;background:var(--plum)}
.map-area{left:300px;top:40px;width:520px;height:300px;border-radius:50%;background:radial-gradient(ellipse at center,var(--plum-soft) 0%,rgba(74,42,90,.6) 45%,rgba(53,26,65,0) 72%)}
.star-area{left:800px;top:148px;width:181px;height:216px;background:radial-gradient(ellipse at 50% 55%,rgba(200,150,60,.32) 0%,rgba(150,100,60,.15) 40%,rgba(53,26,65,0) 72%)}
.rule{left:0;width:981px;height:1px;background:rgba(255,255,255,.18)}
.brand{font-family:Questrial,sans-serif;font-size:27px;line-height:1;color:var(--gold);letter-spacing:.5px;white-space:nowrap}
.mainnav{left:462px;top:66px;font-family:Oswald,sans-serif;font-size:19px;color:#fff;letter-spacing:.3px}
.mainnav span{margin-right:10px}
.mainnav .on{color:var(--gold)}

.search{left:170px;top:122px;width:637px;height:66px;border-radius:5px;background:linear-gradient(var(--gold),var(--gold-deep))}
.search .www{left:30px;top:20px;font-weight:700;font-size:24px;color:var(--plum);letter-spacing:1px}
.search .field{left:108px;top:12px;width:392px;height:42px;border-radius:3px;background:linear-gradient(var(--gold-pale),#fffde0);border:1px solid #e8b820}
.search .go{left:507px;top:12px;width:102px;height:42px;border-radius:3px;background:var(--plum);color:#fff;font-family:Oswald,sans-serif;font-size:19px;text-align:center;line-height:42px}
.filters{left:310px;top:194px;font-size:9px;color:#fff;display:flex;gap:10px}
.cb{display:inline-block;width:9px;height:9px;background:#fff;border:1px solid #999;vertical-align:-1px;margin-right:4px;position:relative}
.cb.on::after{content:"";position:absolute;left:2px;top:0;width:3px;height:6px;border:solid var(--plum);border-width:0 1.5px 1.5px 0;transform:rotate(45deg)}
.caret{display:inline-block;border:3px solid transparent;border-top:4px solid #fff;margin-left:5px;vertical-align:-1px}

.leased{left:170px;top:224px;width:386px;height:76px;border:1px solid var(--gold);border-radius:5px}
.leased h3{position:absolute;left:13px;top:7px;font-family:Questrial,sans-serif;font-weight:400;font-size:17px;color:var(--gold)}
.uncheck{position:absolute;left:223px;top:9px;width:70px;height:16px;border-radius:3px;background:#fff;font-size:9px;font-weight:700;text-align:center;line-height:16px;color:#222}
.tlds{position:absolute;left:13px;top:34px;display:grid;grid-template-columns:repeat(6,62px);row-gap:6px;font-size:9px;color:#fff}

.promo{right:175px;top:221px;text-align:right;font-family:Oswald,sans-serif;color:var(--gold)}
.promo .big{font-size:32px;line-height:34px;font-weight:600}
.promo .mid{font-size:21px;line-height:26px;font-weight:500}
.promo .small{font-size:10px;font-weight:500;color:#fff;margin-top:4px;letter-spacing:.1px}

/* sidebar */
.side{left:140px;top:394px;width:226px;height:445px;background:var(--panel);border:1px solid #d8d8d8;border-radius:5px}
.side .globe{position:absolute;left:12px;top:10px;width:30px;height:30px;border-radius:50%;background:radial-gradient(circle at 35% 35%,#8ec2ff,#1d5fb3)}
.side h2{position:absolute;left:52px;top:14px;font-family:Oswald,sans-serif;font-weight:600;font-size:19px;color:var(--plum)}
.prices{position:absolute;left:12px;top:50px;width:205px;font-size:9px}
.prices .row{display:grid;grid-template-columns:17px 94px 56px 40px;height:14.7px;align-items:center}
.flag{width:11px;height:8px;display:block}
.dot{width:9px;height:9px;border-radius:50%;background:#ccc;display:block}
.prices .name{font-weight:700;color:var(--link)}
.note{position:absolute;left:16px;top:425px;font-size:8px;color:#444}
.note b{color:var(--red)}

/* listing */
.tabs{left:403px;top:391px;display:flex}
.tab{height:34px;border:1px solid #999;border-bottom:none;font-size:11px;text-align:center;line-height:34px;color:#333}
.tab.sel{color:var(--gold-deep);border-color:#eee}
.count{left:389px;top:435px;font-size:12px;color:#555}
.pager{left:415px;top:459px;display:flex}
.pager span{width:51px;height:19px;border:1px solid #bbb;text-align:center;line-height:17px;font-size:12px;color:#333}
.sortsel{left:738px;top:458px;width:103px;height:22px;border:1px solid #bbb;font-size:9.5px;line-height:20px;padding-left:6px;color:#333;white-space:nowrap}
.sortsel::after{content:"";position:absolute;right:4px;top:8px;border:4px solid transparent;border-top:5px solid #222}

.listing{left:389px;top:493px;width:452px;border-collapse:collapse}
.listing th{background:var(--plum);color:#fff;font-weight:400;font-size:12px;height:29px;text-align:left;padding-left:5px}
.listing td{height:34.4px;padding-left:5px;font-size:8px;color:#555}
.listing tr:nth-child(even) td{background:var(--plum-row);color:#ddd}
.listing .dom{font-family:Questrial,sans-serif;font-size:12.5px;color:var(--plum);width:174px}
.listing tr:nth-child(even) .dom{color:#fff}
.fee{display:inline-block;width:56px;height:20px;background:linear-gradient(var(--gold),var(--gold-deep));font-size:11px;color:#7a4b00;text-align:center;line-height:20px}
.offer{display:inline-block;width:57px;height:20px;background:var(--red);color:#fff;font-size:10.5px;text-align:center;line-height:20px;border:1px solid #900}

/* footer */
.footer{left:0;top:1034px;width:981px;height:166px;background:var(--plum)}
.fcol{top:1058px;font-size:9px;color:#ddd;line-height:15.8px}
.fcol b{color:#fff;font-size:9.5px}
.fbottom{top:1170px;font-size:9px;color:#ddd}
</style>
</head>
<body>
<div class="page">

  <div class="abs topbar">
    <a class="active" style="left:169px" href="#">Home</a>
    <a style="left:214px" href="#">Contact</a>
    <a style="left:265px" href="#">Support</a>
    <a style="left:668px" href="#">Login &nbsp;/&nbsp; SignUp</a>
    <div class="social" style="left:751px"><span></span><span></span><span></span></div>
  </div>

  <div class="abs header"></div>
  <div class="abs map-area" role="img" aria-label="Faint dotted world map"></div>
  <div class="abs star-area" role="img" aria-label="Large gold star outline"></div>
  <div class="abs rule" style="top:122px"></div>
  <div class="abs rule" style="top:135px"></div>

  <div class="abs brand" style="left:167px;top:60px">CORVANE DOMAIN</div>

  <div class="abs mainnav"><span class="on">DOMAINS</span><span>/</span><span>HOSTING</span><span>/</span><span>WEBSITES</span><span>/</span><span>WEB TOOLS</span></div>

  <div class="abs search">
    <div class="abs www">www.</div>
    <div class="abs field"></div>
    <div class="abs go">SEARCH</div>
  </div>

  <div class="abs filters">
    <span><i class="cb on"></i>All</span>
    <span><i class="cb"></i>Generic<i class="caret"></i></span>
    <span><i class="cb"></i>European<i class="caret"></i></span>
    <span><i class="cb"></i>Asia-Pacific<i class="caret"></i></span>
    <span><i class="cb"></i>American<i class="caret"></i></span>
    <span><i class="cb"></i>African<i class="caret"></i></span>
  </div>

  <div class="abs leased">
    <h3>Leased domain names</h3>
    <div class="uncheck">Uncheck all</div>
    <div class="tlds">
      <span><i class="cb on"></i>.com.au</span><span><i class="cb"></i>.net.au</span><span><i class="cb"></i>.org.au</span><span><i class="cb"></i>.com</span><span><i class="cb"></i>.net</span><span><i class="cb"></i>.org</span>
      <span><i class="cb on"></i>.co</span><span><i class="cb"></i>.co.nz</span><span><i class="cb"></i>.asia</span><span><i class="cb"></i>.hk</span><span><i class="cb"></i>.sg</span><span><i class="cb"></i>.eu</span>
    </div>
  </div>

  <div class="abs promo">
    <div class="big">SUPERIOR</div>
    <div class="mid">DOMAINS ON LEASE</div>
    <div class="small">AFFORDABLE DOMAIN FOR A SUCCESSFUL BUSINESS</div>
  </div>

  <aside class="abs side">
    <div class="globe"></div>
    <h2>CORVANE DOMAINS</h2>
    <div class="prices">
      <div class="row"><i class="dot"></i><span class="name">World</span><span>.com</span><span>$ 8.70</span></div>
      <div class="row"><i class="dot"></i><span class="name">World</span><span>.net</span><span>$ 8.70</span></div>
      <div class="row"><i class="dot"></i><span class="name">World</span><span>.org</span><span>$ 8.70</span></div>
      <div class="row"><i class="dot"></i><span class="name">World</span><span>.co</span><span>$ 28.10</span></div>
      <div class="row"><i class="dot"></i><span class="name">World</span><span>.me</span><span>$ 32.90</span></div>
      <div class="row"><i class="flag" style="background:linear-gradient(#9cd0f0 33%,#fff 33% 66%,#9cd0f0 66%)"></i><span class="name">Argentina</span><span>.com.ar</span><span>$ 55.20</span></div>
      <div class="row"><i class="dot"></i><span class="name">Asia</span><span>.asia</span><span>$ 19.40</span></div>
      <div class="row"><i class="flag" style="background:#1a2f7a"></i><span class="name">Australia</span><span>.com.au</span><span>$ 9.95</span></div>
      <div class="row"><i class="flag" style="background:linear-gradient(#d22 33%,#fff 33% 66%,#d22 66%)"></i><span class="name">Austria</span><span>.at</span><span>$ 24.10</span></div>
      <div class="row"><i class="flag" style="background:linear-gradient(90deg,#111 33%,#fd0 33% 66%,#d22 66%)"></i><span class="name">Belgium</span><span>.be</span><span>$ 9.70</span></div>
      <div class="row"><i class="flag" style="background:#2a9a3a"></i><span class="name">Brazil</span><span>.com.br</span><span>$ 56.10</span></div>
      <div class="row"><i class="flag" style="background:linear-gradient(90deg,#d22 25%,#fff 25% 75%,#d22 75%)"></i><span class="name">Canada</span><span>.ca</span><span>$ 25.20</span></div>
      <div class="row"><i class="flag" style="background:#d22"></i><span class="name">China</span><span>.cn</span><span>$ 38.70<b style="color:var(--red)">*</b></span></div>
      <div class="row"><i class="flag" style="background:#c12"></i><span class="name">Denmark</span><span>.dk</span><span>$ 32.90</span></div>
      <div class="row"><i class="flag" style="background:#1a3a9a"></i><span class="name">European Union</span><span>.eu</span><span>$ 8.70</span></div>
      <div class="row"><i class="flag" style="background:#fff;border:1px solid #1a3a9a"></i><span class="name">Finland</span><span>.fi</span><span>$ 60.00</span></div>
      <div class="row"><i class="flag" style="background:linear-gradient(90deg,#1a3a9a 33%,#fff 33% 66%,#d22 66%)"></i><span class="name">France</span><span>.fr</span><span>$ 14.10</span></div>
      <div class="row"><i class="flag" style="background:linear-gradient(#111 33%,#d22 33% 66%,#fc0 66%)"></i><span class="name">Germany</span><span>.de</span><span>$ 9.70</span></div>
      <div class="row"><i class="flag" style="background:repeating-linear-gradient(#3a6fc0 0 1.6px,#fff 1.6px 3.2px)"></i><span class="name">Greece</span><span>.gr</span><span>$ 40.20</span></div>
      <div class="row"><i class="flag" style="background:#d22"></i><span class="name">Hong Kong</span><span>.hk</span><span>$ 41.60</span></div>
      <div class="row"><i class="flag" style="background:linear-gradient(#f93 33%,#fff 33% 66%,#1a8a3a 66%)"></i><span class="name">India</span><span>.in</span><span>$ 24.20</span></div>
      <div class="row"><i class="flag" style="background:linear-gradient(#d22 50%,#fff 50%)"></i><span class="name">Indonesia</span><span>.co.id</span><span>$ 49.40</span></div>
      <div class="row"><i class="flag" style="background:linear-gradient(90deg,#1a8a3a 33%,#fff 33% 66%,#f93 66%)"></i><span class="name">Ireland</span><span>.ie</span><span>$ 67.80</span></div>
      <div class="row"><i class="flag" style="background:linear-gradient(#fff 15%,#2a5ac0 15% 28%,#fff 28% 72%,#2a5ac0 72% 85%,#fff 85%)"></i><span class="name">Israel</span><span>.co.il</span><span>$ 44.50</span></div>
      <div class="row"><i class="flag" style="background:linear-gradient(90deg,#1a8a3a 33%,#fff 33% 66%,#d22 66%)"></i><span class="name">Italy</span><span>.it</span><span>$ 44.50</span></div>
    </div>
    <p class="note"><b>*</b> Price shown does not include setup free</p>
  </aside>

  <div class="abs tabs">
    <div class="tab" style="width:109px">ALL DOMAINS</div>
    <div class="tab" style="width:109px;border-left:none">BUY DOMAINS</div>
    <div class="tab sel" style="width:108px">LEASE DOMAINS</div>
  </div>
  <div class="abs count">Displaying 1 - 75 of 63152 Domains</div>
  <div class="abs pager"><span>&gt;</span><span>&raquo;</span></div>
  <div class="abs sortsel">Lease Fee Descen</div>

  <table class="abs listing">
    <thead><tr><th>Domain Name</th><th style="width:134px">Category</th><th style="width:75px">Lease Fee</th><th style="width:69px">Price</th></tr></thead>
    <tbody>
      <tr><td class="dom">CreditTallys.com</td><td>Business and Finance</td><td><span class="fee">$1500</span></td><td><span class="offer">Make Offer</span></td></tr>
      <tr><td class="dom">ReelSerials.com</td><td>Computers and Internet</td><td><span class="fee">$8,500</span></td><td><span class="offer">Make Offer</span></td></tr>
      <tr><td class="dom">ThriftyFlyer.com</td><td>Travel</td><td><span class="fee">$8,500</span></td><td><span class="offer">Make Offer</span></td></tr>
      <tr><td class="dom">VitalScanner.com</td><td>Business and Finance</td><td><span class="fee">$8,500</span></td><td><span class="offer">Make Offer</span></td></tr>
      <tr><td class="dom">MotorBidders.com</td><td>Automotive</td><td><span class="fee">$8,500</span></td><td><span class="offer">Make Offer</span></td></tr>
      <tr><td class="dom">Tapglassly.com</td><td>General</td><td><span class="fee">$8,500</span></td><td><span class="offer">Make Offer</span></td></tr>
      <tr><td class="dom">RelayIndex.com</td><td>Business and Finance</td><td><span class="fee">$8,500</span></td><td><span class="offer">Make Offer</span></td></tr>
      <tr><td class="dom">LevyGuardia.com</td><td>Business and Finance</td><td><span class="fee">$8,500</span></td><td><span class="offer">Make Offer</span></td></tr>
      <tr><td class="dom">DutyForms.com</td><td>Business and Finance</td><td><span class="fee">$8,500</span></td><td><span class="offer">Make Offer</span></td></tr>
      <tr><td class="dom">Tekervani.com</td><td>Automotive</td><td><span class="fee">$8,500</span></td><td><span class="offer">Make Offer</span></td></tr>
      <tr><td class="dom">AlanCarsisi.com</td><td>Computers and Internet</td><td><span class="fee">$8,500</span></td><td><span class="offer">Make Offer</span></td></tr>
      <tr><td class="dom">SofraHizli.com</td><td>Business and Finance</td><td><span class="fee">$8,500</span></td><td><span class="offer">Make Offer</span></td></tr>
      <tr><td class="dom">PlanLoosely.com</td><td>Computers and Internet</td><td><span class="fee">$8,500</span></td><td><span class="offer">Make Offer</span></td></tr>
    </tbody>
  </table>

  <footer class="abs footer"></footer>
  <div class="abs brand" style="left:167px;top:1074px">CORVANE DOMAIN</div>
  <div class="social" style="left:304px;top:1124px;position:absolute"><span></span><span></span><span></span></div>

  <div class="abs fcol" style="left:441px"><b>Domains</b><br>Renew domains<br>Transfer domains<br>Domain privacy<br>Back order domains</div>
  <div class="abs fcol" style="left:550px"><b>Hosting</b><br>Web hosting<br>Email hosting<br>DNS hosting<br>Virtual servers</div>
  <div class="abs fcol" style="left:642px"><b>Web Sites</b><br>Web builders<br>Custom web sites<br>SSL certificates<br>Logo design</div>
  <div class="abs fcol" style="left:744px"><b>Web Tools</b><br>Search submissions<br>Email marketing</div>

  <div class="abs fbottom" style="left:167px">Terms of Use &nbsp;|&nbsp; Monitoring availability &nbsp;|&nbsp; Knowledge Base</div>
  <div class="abs fbottom" style="left:592px">Copyright 2014. CORVANE DOMAIN &nbsp;All Rights Reserved.</div>

</div>
</body>
</html>
```